Business Card for a Life Coaching Company

BRAVOPEAK is a Life Coaching company that was initiated to support people who want to transform thier life or ana aspect of it.
our slogan is : "Dream. Believe. Succeed"
our logo is uploaded.
The name of the company implies that leadership, strength and wisdom required to change your life.
We want an attractive business card that would give an impression of reliability, support and change. so we really want it unique. Here are some examples of unique cards:

http://www.cardcraftvault.example/2009/05/100-really-creative-business-cards/

BravoPeak is a life coaching organization focusing on individual transformation through the application of relevant and timeless principles of success.  BravoPeak believes that real, sustainable life transformations are brought about by tuning into the timeless wisdom we each carry in our hearts while boldy acting in the direction of our dreams.

Contacts on the card:
Address: 7 Tarek Nour El Dine Heliopolis Cairo Egypt
Tel: +202 24 71 38 52
Fax: +202 24 71 38 17
Mobile: +2 012 684 2097 (Dalia Soliman)
+2 0199915815 (Tariq Bhatti)

By the way, our temporary website is http://www.bravopeak.example

We have attached an .eps file with various configurations of our logo.

```html
<!DOCTYPE html>
<html lang="en">
<head>
<meta charset="utf-8">
<title>BravoPeak Business Card</title>
<link rel="stylesheet" href="https://fonts.googleapis.com/css2?family=Crimson+Text&display=swap">
<style>
  :root {
    --backdrop: #e6e5e6;
    --card: #ffffff;
    --brand-orange: #ff6a00;
    --text-orange: #f26a12;
    --logo-grey: #9a9a9a;
  }
  * { margin: 0; padding: 0; box-sizing: border-box; }
  html, body {
    width: 1050px;
    height: 1200px;
    overflow: hidden;
    background: var(--backdrop);
    font-family: "Crimson Text", Georgia, serif;
  }
  .canvas { position: relative; width: 1050px; height: 1200px; }
  .card {
    position: absolute;
    left: 190px;
    width: 680px;
    height: 390px;
    background: var(--card);
    overflow: hidden;
  }
  .card-front { top: 165px; }
  .card-back { top: 620px; width: 678px; height: 388px; }

  .brand {
    position: absolute;
    left: 34px;
    top: 133px;
    display: flex;
    align-items: center;
    gap: 14px;
  }
  .brand-mark {
    flex: none;
    width: 54px;
    height: 54px;
    border-radius: 50%;
    background: var(--brand-orange);
  }
  .brand-name {
    display: block;
    color: var(--logo-grey);
    font-size: 50px;
    line-height: 52px;
    white-space: nowrap;
  }
  .brand-name span { display: block; }
  .slogan-box {
    position: absolute;
    left: 286px;
    top: 161px;
    width: 400px;
    height: 51px;
    border: 2px solid var(--brand-orange);
    color: var(--text-orange);
    font-size: 25px;
    line-height: 47px;
    padding-left: 13px;
    white-space: nowrap;
  }

  .contact {
    position: absolute;
    left: 0;
    top: 79px;
    width: 402px;
    text-align: center;
    color: var(--text-orange);
    font-size: 20px;
    line-height: 30px;
    white-space: nowrap;
  }
  .contact p { margin: 0; }
  .contact .address { margin-bottom: 26px; }
  .contact .people p { line-height: 31px; }
  .contact .people { margin-bottom: 23px; }
  .contact .lines p { line-height: 28px; }
  .contact .lines { margin-bottom: 18px; }
  .ornament-panel {
    position: absolute;
    left: 395px;
    top: 0;
    width: 283px;
    height: 388px;
    background: linear-gradient(135deg, #ff6a00 0%, #ff7a1a 50%, #ff6a00 100%);
  }
</style>
</head>
<body>
<main class="canvas">
  <section class="card card-front">
    <div class="brand">
      <span class="brand-mark"></span>
      <span class="brand-name"><span>BRAVO</span><span>PEAK</span></span>
    </div>
    <div class="slogan-box">"Dream. Believe. Succeed"</div>
  </section>

  <section class="card card-back">
    <div class="contact">
      <p class="address">7 Tarek Nour El Dine Heliopolis Cairo Egypt</p>
      <div class="people">
        <p>(Dalia Soliman)+2 012 684 2097</p>
        <p>(Tariq Bhatti)+2 0197328406</p>
      </div>
      <div class="lines">
        <p>Tel: +202 24 71 38 52</p>
        <p>Fax: +202 24 71 38 17</p>
      </div>
      <p class="web">www.bravopeak.example</p>
    </div>
    <div class="ornament-panel" role="img" aria-label="Orange panel with white flowing floral scroll ornament"></div>
  </section>
</main>
</body>
</html>
```